Mobile App UI for Telecommunications/Hosting Company

We are about to convert our existing self-service Customer Portal into a mobile phone application and need an elegant and professional UI/UX design. Our company provides telecommunication (voice/mobile/data) and hosting services to medium-sized business. The primary purpose of the application is to view trouble tickets, alerts, orders, and performance charts. This application is available to customers only - not the general public.

Please provide a UI design suitable for display on iPhone/Android devices. The attached document includes a proposed screen flow. You are free to design your own screens to display the same information elegantly.
Updates

Please note that the design should be based on the wireframes in the Word document, not the screenshots.  The screenshots are just to show our existing web portal look & feel.

Also, just a few screens are required for initial submission (3 would be great).

Thanks,
Dermot.

Target Market(s)

IT Managers away from their desk and using a mobile phone application.
Adult males from technical background aged 30-50.
Customers of Brindlewood Networks have access to this application (not the general public). This is a self-service portal for customers only.

Industry/Entity Type

Business

Colors
0592cd
33a6d7
85cae6
cadf82
fde08a

Requirements
Must have
• Please look at the screenshots from our current Customer Portal site (part of the project brief). The mobile app does not have to look the same, but should follow a similar style.

Please check out our company web site at www.brindlewoodnetworks.example (this site is not the customer portal and has a different look at feel) to understand what Brindlewood Networks does.
Nice to have
• Sharing capabilities via email/SMS.
A nice background image to make it stand out
The colours selected below are a guide only as they are similar to the corporate colours
- The priority is something that works on a phone - a design extendable to tablets is a nice to have as our existing web site looks OK on a tablet..

```html
<!DOCTYPE html>
<html lang="en">
<head>
<meta charset="utf-8">
<title>Brindlewood View – Mobile App Screens</title>
<link rel="stylesheet" href="https://fonts.googleapis.com/css2?family=Lato:wght@400;700&display=swap">
<style>
:root{
  --canvas:#cdd3d6;
  --blue:#0592cd;
  --blue-mid:#33a6d7;
  --blue-light:#85cae6;
  --green:#a9cf2e;
  --yellow:#fde08a;
  --yellow-deep:#f7cd55;
  --dark:#474747;
  --ink:#555b60;
  --muted:#8f969b;
  --line:#e2e5e7;
  --orange:#f0771a;
  --brand:#2f6fa8;
  --white:#ffffff;
}
*{box-sizing:border-box;margin:0;padding:0}
html,body{width:821px;height:1200px;overflow:hidden}
body{background:var(--canvas);font-family:"Lato",Arial,sans-serif;position:relative;color:var(--ink)}
.screen{position:absolute;background:var(--white);overflow:hidden;box-shadow:0 1px 2px rgba(0,0,0,.12)}
.abs{position:absolute}
.brand{display:flex;align-items:center;gap:10px;position:absolute}
.brand-dot{width:38px;height:38px;border-radius:50%;background:var(--blue-mid)}
.brand-name{font-size:24px;font-weight:400;color:var(--brand);letter-spacing:-.3px}

/* Login screen */
.login{left:51px;top:59px;width:337px;height:599px}
.status-bar{top:0;left:0;width:100%;height:24px;background:var(--blue);color:var(--white);font-size:12px;display:flex;align-items:center;justify-content:space-between;padding:0 8px}
.app-bar{top:24px;left:0;width:100%;height:44px;background:var(--blue);color:var(--white);display:flex;align-items:center;justify-content:center;font-size:15px}
.app-bar svg{position:absolute;top:11px}
.login .brand{left:45px;top:95px}
.login-panel{top:166px;left:0;width:100%;height:382px;background:var(--dark)}
.welcome{width:100%;text-align:center;top:38px;color:var(--white);font-size:19px;font-weight:700}
.field{left:25px;width:291px;height:50px;background:#f2f2f2;font-size:16px;display:flex;align-items:center;padding-left:19px;color:var(--ink)}
.field-user{top:96px;font-weight:700}
.field-pass{top:147px;letter-spacing:3px;font-size:18px}
.btn-signin{left:25px;top:223px;width:291px;height:50px;background:var(--green);color:var(--white);font-size:19px;font-weight:700;display:flex;align-items:center;justify-content:center}
.remember{left:25px;top:323px;display:flex;align-items:center;gap:10px;color:#e6e6e6;font-size:15px}
.checkbox{width:15px;height:15px;background:var(--white)}
.forgot{right:22px;top:323px;color:#e6e6e6;font-size:15px}
.login-footer{top:548px;left:0;width:100%;height:51px;background:#e8e8e8}
.social{top:14px;width:26px;height:26px;border-radius:50%}
.social-outline{border:1px solid #8d8d8d}

/* Statement screen */
.statement{left:431px;top:59px;width:336px;height:631px;background:transparent;box-shadow:none}
.st-header{top:0;left:0;width:336px;height:69px;background:var(--white)}
.st-header .brand{left:70px;top:18px}
.st-title{top:69px;left:0;width:336px;height:47px;background:linear-gradient(90deg,#eef5f8,#f8fbfc 50%,#eef5f8);color:var(--orange);font-size:17px;display:flex;align-items:center;justify-content:center}
.acc-row{left:0;width:336px;height:54px;background:var(--white);box-shadow:0 1px 2px rgba(0,0,0,.15)}
.acc-toggle{position:absolute;left:0;top:0;width:43px;height:100%;background:var(--blue);display:flex;align-items:center;justify-content:center}
.acc-label{position:absolute;left:66px;top:0;height:100%;display:flex;align-items:center;font-size:15px;color:var(--muted)}
.acc-table{left:43px;top:233px;width:293px;height:226px;background:var(--white);box-shadow:0 1px 2px rgba(0,0,0,.15)}
.acc-gutter{left:0;top:233px;width:43px;height:226px;background:#eef5f8}
.t-row{position:absolute;left:0;width:293px;height:43px;border-bottom:1px solid var(--line);font-size:13px;color:var(--muted)}
.t-row span{position:absolute;top:14px}
.t-head{color:var(--blue);font-size:13px}
.c1{left:26px}.c2{left:104px}.c3{left:185px}
.row-active::before{content:"";position:absolute;left:0;top:0;width:6px;height:100%;background:var(--yellow-deep)}

/* Menu screen */
.menu{left:51px;top:695px;width:337px;height:460px;background:linear-gradient(160deg,#f7fbfd 0%,#f3ecec 45%,#ebe8ea 100%)}
.menu .brand{left:52px;top:17px}
.menu-item{left:0;width:337px;height:50px;border-bottom:1px solid #dcdcdc;display:flex;align-items:center;font-size:16px;color:var(--ink)}
.menu-item svg.icon{position:absolute;left:18px}
.menu-item .label{position:absolute;left:58px}
.menu-item svg.chev{position:absolute;right:16px}
.menu-item.is-active{background:var(--yellow)}
.signout{left:0;top:418px;width:337px;height:42px;background:linear-gradient(90deg,#f9d468,#fde08a 50%,#f9d468);display:flex;align-items:center;justify-content:center;gap:14px;font-size:15px;color:var(--ink)}
</style>
</head>
<body>

<!-- Login -->
<section class="screen login">
  <div class="abs status-bar"><span>●●●○○ Northwave &nbsp;≋</span><span>4:21 PM</span><span>100% ▭</span></div>
  <header class="abs app-bar">
    <svg style="left:15px" width="22" height="22" viewBox="0 0 22 22"><circle cx="11" cy="11" r="10" fill="none" stroke="#fff" stroke-width="1.5"/><path d="M6.5 7.5h9M6.5 11h9M6.5 14.5h9" stroke="#fff" stroke-width="1.5"/></svg>
    Brindlewood View
    <svg style="right:15px" width="22" height="22" viewBox="0 0 22 22"><circle cx="11" cy="11" r="10" fill="none" stroke="#fff" stroke-width="1.5"/><path d="M11 5.5v11M5.5 11h11" stroke="#fff" stroke-width="1.5"/></svg>
  </header>
  <div class="brand"><span class="brand-dot"></span><span class="brand-name">brindlewoodview</span></div>
  <div class="abs login-panel">
    <h1 class="abs welcome">Welcome</h1>
    <div class="abs field field-user">Username</div>
    <div class="abs field field-pass">●●●●●●●●</div>
    <div class="abs btn-signin">Sign in</div>
    <label class="abs remember"><span class="checkbox"></span>Remember me</label>
    <span class="abs forgot">I forgot!</span>
  </div>
  <footer class="abs login-footer">
    <svg class="abs" style="left:19px;top:12px" width="26" height="26" viewBox="0 0 26 26"><path d="M2 13L13 3l11 10M5 11v12h6v-7h4v7h6V11" fill="none" stroke="#33a6d7" stroke-width="1.5"/></svg>
    <span class="abs social social-outline" style="left:89px"></span>
    <span class="abs social" style="left:136px;background:#33a6d7"></span>
    <span class="abs social" style="left:183px;background:#e5533f"></span>
    <span class="abs social social-outline" style="left:230px"></span>
  </footer>
</section>

<!-- Statement history -->
<section class="screen statement">
  <header class="abs st-header">
    <svg class="abs" style="left:16px;top:33px" width="22" height="22" viewBox="0 0 22 22"><circle cx="11" cy="11" r="10" fill="none" stroke="#8f969b" stroke-width="1.3"/><path d="M12.5 6.5L8 11l4.5 4.5M8 11h7" fill="none" stroke="#8f969b" stroke-width="1.3"/></svg>
    <div class="brand"><span class="brand-dot"></span><span class="brand-name">brindlewoodview</span></div>
    <svg class="abs" style="left:300px;top:33px" width="22" height="22" viewBox="0 0 22 22"><circle cx="9" cy="9" r="7" fill="none" stroke="#8f969b" stroke-width="1.4"/><path d="M14 14l6 6" stroke="#8f969b" stroke-width="1.6"/></svg>
  </header>
  <h2 class="abs st-title">STATEMENT HISTORY</h2>

  <div class="abs acc-row" style="top:116px"><span class="acc-toggle"><svg width="14" height="11"><path d="M0 0h14L7 11z" fill="#fff"/></svg></span><span class="acc-label">Statement History Billing Month</span></div>
  <div class="abs acc-row" style="top:178px"><span class="acc-toggle"><svg width="14" height="11"><path d="M0 11h14L7 0z" fill="#fff"/></svg></span><span class="acc-label">Account History</span></div>

  <div class="abs acc-gutter"></div>
  <div class="abs acc-table">
    <div class="t-row t-head" style="top:0"><span class="c1">MONTH</span><span class="c2">INVOICE</span><span class="c3">Billed(excl GST)</span></div>
    <div class="t-row row-active" style="top:43px"><span class="c1">Dec 2013</span><span class="c2">252352</span><span class="c3">$235,205,88</span></div>
    <div class="t-row" style="top:86px"><span class="c1">Nov 2013</span><span class="c2">252352</span><span class="c3">$235,205,88</span></div>
    <div class="t-row" style="top:129px"><span class="c1">Feb2013</span><span class="c2">252352</span><span class="c3">$235,205,88</span></div>
    <div class="t-row" style="top:172px;border-bottom:0"><span class="c1">Mar 2013</span><span class="c2">252352</span><span class="c3">$235,205,88</span></div>
  </div>

  <div class="abs acc-row" style="top:461px"><span class="acc-toggle"><svg width="14" height="11"><path d="M0 0h14L7 11z" fill="#fff"/></svg></span><span class="acc-label">Account Name</span></div>
  <div class="abs acc-row" style="top:519px"><span class="acc-toggle"><svg width="14" height="11"><path d="M0 0h14L7 11z" fill="#fff"/></svg></span><span class="acc-label">Account Sumary</span></div>
  <div class="abs acc-row" style="top:577px"><span class="acc-toggle"><svg width="14" height="11"><path d="M0 0h14L7 11z" fill="#fff"/></svg></span><span class="acc-label">Transaction History</span></div>
</section>

<!-- Menu -->
<nav class="screen menu">
  <div class="brand"><span class="brand-dot"></span><span class="brand-name">brindlewoodview</span></div>

  <div class="abs menu-item" style="top:71px">
    <svg class="icon" width="24" height="24" viewBox="0 0 24 24"><path d="M20 9a8.5 8.5 0 0 0-15-2M4 15a8.5 8.5 0 0 0 15 2M4 3v4h4M20 21v-4h-4" fill="none" stroke="#33a6d7" stroke-width="1.3"/></svg>
    <span class="label">Services</span><svg class="chev" width="9" height="16"><path d="M1 1l7 7-7 7" fill="none" stroke="#777" stroke-width="1.3"/></svg>
  </div>
  <div class="abs menu-item is-active" style="top:120px">
    <svg class="icon" width="24" height="24" viewBox="0 0 24 24"><path d="M9 2h12v20H9M2 12h12M10 8l4 4-4 4" fill="none" stroke="#33a6d7" stroke-width="1.3"/></svg>
    <span class="label">Billing</span><svg class="chev" width="9" height="16"><path d="M1 1l7 7-7 7" fill="none" stroke="#777" stroke-width="1.3"/></svg>
  </div>
  <div class="abs menu-item" style="top:170px">
    <svg class="icon" width="24" height="24" viewBox="0 0 24 24"><rect x="1.5" y="5" width="21" height="14" fill="none" stroke="#33a6d7" stroke-width="1.3"/><path d="M1.5 5l10.5 8 10.5-8M1.5 19l8-7M22.5 19l-8-7" fill="none" stroke="#33a6d7" stroke-width="1.3"/></svg>
    <span class="label">Orders</span><svg class="chev" width="9" height="16"><path d="M1 1l7 7-7 7" fill="none" stroke="#777" stroke-width="1.3"/></svg>
  </div>
  <div class="abs menu-item" style="top:220px">
    <svg class="icon" width="24" height="24" viewBox="0 0 24 24"><circle cx="12" cy="12" r="10.5" fill="none" stroke="#33a6d7" stroke-width="1.3"/><path d="M7 12.5l3.5 3.5L17 9" fill="none" stroke="#33a6d7" stroke-width="1.3"/></svg>
    <span class="label">Tickets</span><svg class="chev" width="9" height="16"><path d="M1 1l7 7-7 7" fill="none" stroke="#777" stroke-width="1.3"/></svg>
  </div>
  <div class="abs menu-item" style="top:270px">
    <svg class="icon" width="24" height="24" viewBox="0 0 24 24"><circle cx="12" cy="8" r="5" fill="none" stroke="#33a6d7" stroke-width="1.3"/><path d="M2 22c1-5 5-7 10-7s9 2 10 7z" fill="none" stroke="#33a6d7" stroke-width="1.3"/></svg>
    <span class="label">Self Service</span>
  </div>
  <div class="abs menu-item" style="top:320px">
    <svg class="icon" width="24" height="24" viewBox="0 0 24 24"><circle cx="12" cy="12" r="3.5" fill="none" stroke="#33a6d7" stroke-width="1.3"/><path d="M12 2v4M12 18v4M2 12h4M18 12h4M5 5l3 3M16 16l3 3M5 19l3-3M16 8l3-3" stroke="#33a6d7" stroke-width="1.3"/><circle cx="12" cy="12" r="7" fill="none" stroke="#33a6d7" stroke-width="1.3"/></svg>
    <span class="label">Settings</span><svg class="chev" width="9" height="16"><path d="M1 1l7 7-7 7" fill="none" stroke="#777" stroke-width="1.3"/></svg>
  </div>
  <div class="abs menu-item" style="top:370px;border-bottom:0">
    <svg class="icon" width="24" height="24" viewBox="0 0 24 24"><circle cx="12" cy="12" r="10.5" fill="none" stroke="#33a6d7" stroke-width="1.3"/><path d="M9 9.5a3 3 0 1 1 4 2.8c-.7.3-1 .9-1 1.7v.5" fill="none" stroke="#33a6d7" stroke-width="1.3"/><circle cx="12" cy="17.5" r=".9" fill="#33a6d7"/></svg>
    <span class="label">Help</span><svg class="chev" width="9" height="16"><path d="M1 1l7 7-7 7" fill="none" stroke="#777" stroke-width="1.3"/></svg>
  </div>

  <div class="abs signout">
    <svg width="22" height="20" viewBox="0 0 22 20"><path d="M9 1h12v18H9M1 10h12M5 6l-4 4 4 4" fill="none" stroke="#555b60" stroke-width="1.3"/></svg>
    Sign Out
  </div>
</nav>

</body>
</html>
```